Letterhead for New Orthopaedic Surgery Practice

My husband and I are starting our own practice named RB Spine & Vitality Center. We would like to create a nice simple but high class letterhead that doesn't use too much solid color ink when printing. I like the colors dark blue, gold, yellow. Open to other suggestions. We will need to list him and I both on the top of the letterhead. Here is the important information:
Lucinda Perrow, M.D. - Hand and Upper Extremity Surgery
Abena Quist, M.D. - Hip & Knee Replacement/General Orthopaedic Surgery
Location: 18735 North Harlow Pkwy
Maple Hollow, FL 33950
Phone: 954-218-4650
Fax: 954-582-1346
Email: info@myrbspine.com

The only thing is that the phone and fax numbers will change once we get into our space. I just want to get the design started. I am including several documents which are my previous practice letterhead, my current procedure room letterhead, and our new Logo. The other letterheads are just for examples but please think outside of the box! We would love to see some great designs.

Colors
0054AA
0677BA
7BADD7
CADEEF
E8F1F8
0094D4
00A9DD
6FCCEA
C7EBF8
E9F6FB

Requirements
Must have
• class, elegance, luxury

```html
<!DOCTYPE html>
<html lang="en">
<head>
<meta charset="utf-8">
<title>RB Spine &amp; Vitality Center – Letterhead</title>
<link rel="stylesheet" href="https://fonts.googleapis.com/css2?family=Questrial&display=swap">
<style>
  :root {
    --brand-blue: #0624a6;
    --brand-gold: #ffc800;
    --paper: #ffffff;
    --backdrop: #ececec;
  }
  * { margin: 0; padding: 0; box-sizing: border-box; }
  html, body {
    width: 977px;
    height: 1200px;
    overflow: hidden;
    background: var(--backdrop);
  }
  body {
    font-family: "Questrial", sans-serif;
    color: var(--brand-blue);
    position: relative;
  }
  .letterhead {
    position: absolute;
    left: 64px;
    top: 0;
    width: 849px;
    height: 1200px;
    background: var(--paper);
    overflow: hidden;
  }
  .wave { position: absolute; left: 0; top: 0; width: 849px; height: 1200px; }
  .wave .gold { fill: var(--brand-gold); }
  .wave .blue { fill: var(--brand-blue); }

  .practice-name {
    position: absolute;
    top: 112px;
    left: 0;
    width: 849px;
    text-align: center;
    font-size: 27px;
    line-height: 34px;
    font-weight: 400;
    letter-spacing: 2px;
    text-transform: uppercase;
  }

  .physician {
    position: absolute;
    top: 225px;
  }
  .physician--left { left: 75px; }
  .physician--right { left: 514px; }
  .physician__name {
    font-size: 34px;
    line-height: 40px;
    font-weight: 400;
  }
  .physician__specialty {
    font-size: 18.5px;
    line-height: 23px;
  }
  .physician-divider {
    position: absolute;
    left: 441px;
    top: 220px;
    width: 1.5px;
    height: 97px;
    background: var(--brand-blue);
  }

  .footer-rule {
    position: absolute;
    left: 78px;
    top: 1087px;
    width: 692px;
    height: 1.5px;
    background: var(--brand-blue);
  }
  .contact {
    position: absolute;
    display: flex;
    align-items: center;
    font-size: 14px;
    white-space: nowrap;
  }
  .contact svg { fill: var(--brand-blue); flex: none; }
  .contact--phone { left: 122px; top: 1109px; }
  .contact--fax { left: 122px; top: 1153px; }
  .contact--email { left: 414px; top: 1109px; }
  .contact--address { left: 414px; top: 1150px; }
  .contact--phone span, .contact--fax span { margin-left: 16px; }
  .contact--email span { margin-left: 22px; }
  .contact--address span { margin-left: 10px; }
</style>
</head>
<body>
<main class="letterhead">
  <svg class="wave" viewBox="0 0 849 1200" aria-hidden="true">
    <path class="gold" d="M0 0 H37 C26 150 10 330 38 460 C72 620 62 820 0 1005 Z"/>
    <path class="blue" d="M0 0 H25 C14 150 -2 330 26 460 C58 620 48 830 0 990 Z"/>
    <path class="gold" d="M849 197 C815 330 785 480 785 610 C785 680 790 720 798 750 C815 830 830 960 812 1200 H849 Z"/>
    <path class="blue" d="M849 225 C825 340 798 480 798 610 C798 680 803 720 812 750 C828 830 840 960 823 1200 H849 Z"/>
  </svg>

  <h1 class="practice-name">RB Spine &amp; Vitality<br>Center</h1>

  <section class="physician physician--left">
    <h2 class="physician__name">Lucinda Perrow, M.D.</h2>
    <p class="physician__specialty">Hand and Upper Extremity Surgery</p>
  </section>
  <div class="physician-divider"></div>
  <section class="physician physician--right">
    <h2 class="physician__name">Abena Quist, M.D.</h2>
    <p class="physician__specialty">Hip &amp; Knee Replacement<br>General Orthopaedic Surgery</p>
  </section>

  <div class="footer-rule"></div>

  <div class="contact contact--phone">
    <svg width="22" height="22" viewBox="0 0 24 24" aria-hidden="true"><path d="M6.6 10.8c1.4 2.8 3.8 5.1 6.6 6.6l2.2-2.2c.3-.3.7-.4 1-.2 1.1.4 2.3.6 3.6.6.6 0 1 .4 1 1V20c0 .6-.4 1-1 1C10.6 21 3 13.4 3 4c0-.6.4-1 1-1h3.5c.6 0 1 .4 1 1 0 1.3.2 2.5.6 3.6.1.3 0 .7-.2 1z"/></svg>
    <span>954-218-4650</span>
  </div>
  <div class="contact contact--fax">
    <svg width="26" height="26" viewBox="0 0 26 26" aria-hidden="true"><path d="M7 2h10l2 2v5h-1.6V4.7L16.3 3.6H8.6V9H7zM3 9.5h20c1 0 1.8.8 1.8 1.8v8.2c0 1-.8 1.8-1.8 1.8h-2.5v-1.5H23c.2 0 .3-.1.3-.3v-8.2c0-.2-.1-.3-.3-.3H3c-.2 0-.3.1-.3.3v8.2c0 .2.1.3.3.3h2.5v1.5H3c-1 0-1.8-.8-1.8-1.8v-8.2c0-1 .8-1.8 1.8-1.8zM6.5 15h13v9.5h-13zm1.5 1.5V23h10v-6.5zm1.5 1.3h7v1h-7zm0 2h7v1h-7zM20.5 12a1 1 0 1 1 0 2 1 1 0 0 1 0-2z"/></svg>
    <span>954-582-1346</span>
  </div>
  <div class="contact contact--email">
    <svg width="20" height="15" viewBox="0 0 20 15" aria-hidden="true"><path d="M0 0h20v15H0zm1.2 1.2v12.6h17.6V1.2zm.4.3L10 8.2l8.4-6.7.8.9L10 9.8.8 2.4zm-.3 11.6 6.3-5.6.8.8-6.3 5.6zm17.4 0-6.3-5.6-.8.8 6.3 5.6z"/></svg>
    <span>info@myrbspine.com</span>
  </div>
  <div class="contact contact--address">
    <svg width="14" height="21" viewBox="0 0 14 21" aria-hidden="true"><path d="M7 0C3.1 0 0 3.1 0 7c0 5 7 14 7 14s7-9 7-14c0-3.9-3.1-7-7-7zm0 9.5A2.5 2.5 0 1 1 7 4.5a2.5 2.5 0 0 1 0 5z"/></svg>
    <span>18735 North Harlow Pkwy, Maple Hollow, FL 33950</span>
  </div>
</main>
</body>
</html>
```